lumavista web design

- Company / Site Description
We are developing a website that will allow anyone in Europe to find in one click, cultural things to do (Exhibition, Museum, Monument, Zoo, Aquarium, Archaeological site…) with friends or family, and to organize the visit (book a ticket / a private visit, book a restaurant nearby…).

Examples
1. You're in London with your girlfriend, it's saturday 10 am, you have two hours to spend and you want to see an exhibition. We provide you in one click all the exhibition matching your location / time and date.

2. You're in Berlin with some friends, it's thursday night you want to go out, but you don't know what to do. We provide you a list of experience, you can select for instance "I want to be on top of the world", and we show you a list of venues matching the selected experience / date / time /location of your request.

- Brand name : Lumavista
- Activity : Cultural Leisure, cultural entertainment

- Target audience
Broad target will be between 20 and 55. Core target will be between 25 and 40. Most likely to live in a city and in Europe.

- Behaviours and preferences
Our user is under time constraint (few minutes to find and choose his visit), idea constraint (is not sure about what to do and see) and money constraint.
He wants to have an easy to use website, not cluttered with information, focussed on added value information. He wants to have a website which is modern, fun and elegant that he will deem as professional and trustworthy.

- Our expectations (Do’s and Don’t)
We want to move away from traditional design. We want some OUT OF THE BOX design. Think of a website design that will look like an app design.
We want to make an awesome / extra ordinary /remember-able design. The design must be so cool, that the user wants to come back to the site. In two words: THINK EXTRAORDINARY.
You can use photos to help the user understand functions. If you use photo, use creative commons license photo.
Avoid black colors

- Functional Requirements
We need Four pages:
1. Home Page (desktop and mobile version): it’s both the homepage and the assistant page. This page will allow the user to find in one click his visit (please refer to the pdf file Assistant home page). The page must be self-explanatory for a first time user.
2. Assistant result page (desktop version): it’s the page that display the results found by the assistant based on the criteria search (please refer to the pdf file mockup - Assistant result page)
3. Site / Event page (desktop version): it’s the page that display each result information (please refer to the pdf file mockup – Event / Site Page)
The pdf files list all the elements include in each page + gives you a mockup of each page (just to put in perspective the element required). You are completely free about the design.
We don’t have the logo yet. Use a dummy logo for your page design.
The selected winner can expect to work with us immediately after the contest and on a on a regular basis later on.

- Technical Requirements
No Flash
For the winner, we will manage the CSS you will just need to provide :
. One PSD file containing all the pages
. Inside the PSD file we want for each page two groups: the first group will embed the desktop design, the second group will embed the responsive mobile design (Home Page only).
In total there should be 4 groups inside the PSD file (3 desktop groups, 1 mobile group).
Each group must contain all the elements specified in the pdf file

Website we like
http://demo.pallorthemes.example/?theme=Vuntel
http://rosetta.quilbershop.example/#home
http://blogsite.trask.moveldock.example/2/
http://demo.pallorthemes.example/?theme=Obelune
http://www.gravonix.example/themes/tallow/
http://skinmarket.example/item/kelp-responsive-photography-blog-theme/full_screen_preview/8817206
http://products.qdvworks.example/?product=example
http://uk.tavershaw.example

Reason: Due to the request of several designers, we have agreed to add 7 additional days to the contest deadline. Thank you. The lumavista team

Reason: We still need to collect all the votes. Sorry for the delay.

Reason: Hello, We extend the contest deadline, in order to collect all the votes from the poll. We should have everything finalized by sunday. Thank you lumavista team

```html
<!DOCTYPE html>
<html lang="en">
<head>
<meta charset="utf-8">
<title>Lumavista — Find a place to stay</title>
<link href="https://fonts.googleapis.com/css2?family=Open+Sans:wght@400;600;700&family=Ubuntu:wght@400;500;700&family=Rokkitt:wght@400&display=swap" rel="stylesheet">
<style>
:root{
  --bar:#2b2d2e;
  --teal:#1b98a0;
  --teal-deep:#0f6c74;
  --teal-text:#17818b;
  --cyan:#27c1cf;
  --green:#2e9b3a;
  --panel:rgba(52,52,52,.93);
  --ink:#3a3a3a;
  --muted:#8c8c8c;
  --line:#dedede;
  --foot:#2a2e37;
  --foot-deep:#22252c;
  --white:#ffffff;
}
*{box-sizing:border-box;margin:0;padding:0}
html,body{width:1200px;height:2446px;overflow:hidden}
body{position:relative;background:var(--white);font-family:"Open Sans",Arial,sans-serif;color:var(--ink)}
.abs{position:absolute}

/* header */
.topbar{left:0;top:0;width:1200px;height:72px;background:var(--bar)}
.brand{left:111px;top:14px;font-family:"Rokkitt",Georgia,serif;font-size:36px;color:#d8d8d8;line-height:40px}
.nav-assistant{left:497px;top:19px;width:105px;height:35px;background:var(--cyan);color:#fff;font-size:15px;line-height:35px;text-align:center}
.nav-fav{left:624px;top:19px;color:#fff;font-size:15px;line-height:35px}
.search{left:750px;top:19px;width:189px;height:35px;background:#111;color:#888;font-size:13px;line-height:35px;padding-left:10px}
.search svg{position:absolute;right:10px;top:9px}
.avatar{left:951px;top:14px;width:44px;height:44px;border-radius:50%;background:linear-gradient(#c9a27f,#e8d2c0);border:2px solid #fff}
.login{left:1004px;top:19px;color:#fff;font-size:15px;line-height:35px}
.lang{left:940px;top:72px;width:149px;height:20px;background:#f4f4f4;border:1px solid #bbb;font-size:12px;line-height:18px;padding-left:6px;z-index:3}
.lang .flag{display:inline-block;width:16px;height:10px;background:linear-gradient(#b22 0 50%,#eee 50%);margin-right:4px;vertical-align:-1px}
.lang .caret{position:absolute;right:2px;top:2px;width:14px;height:14px;border:1px solid #888;font-size:8px;text-align:center;line-height:13px}

/* hero */
.hero-photo{left:0;top:72px;width:1200px;height:800px;background:linear-gradient(100deg,#b9a79a 0%,#8a6e62 25%,#c9d6e2 45%,#e7e2da 60%,#9c7b6a 80%,#6d5c55 100%)}
.fast-contact{left:1167px;top:261px;width:33px;height:130px;background:#3b3b3b;color:#fff;font-size:13px;font-weight:700;letter-spacing:1px;writing-mode:vertical-rl;text-align:center;line-height:33px}
.dot{width:20px;height:20px;border-radius:50%;background:#9a9a9a;left:1144px}
.dot.on{width:38px;height:38px;left:1135px;top:416px;background:var(--cyan);color:#fff;font-size:17px;font-weight:600;text-align:center;line-height:38px;border:3px solid #fff}
.finder{left:773px;top:484px;width:317px;height:388px;background:var(--panel);font-family:"Ubuntu",Arial,sans-serif;color:#fff}
.finder h1{position:absolute;left:9px;top:10px;font-weight:400;font-size:26px;letter-spacing:.3px}
.finder .pitch{position:absolute;left:9px;top:44px;font-size:18px;line-height:22px}
.field{position:absolute;height:30px;background:#fff;color:#666;font-size:13px;line-height:30px;padding-left:12px;font-family:"Open Sans",Arial,sans-serif;overflow:hidden}
.field::after{content:"";position:absolute;right:0;top:0;border-style:solid;border-width:0 12px 12px 0;border-color:transparent var(--cyan) transparent transparent}
.check{position:absolute;left:9px;font-size:12px;font-family:"Open Sans",Arial,sans-serif}
.check i{display:inline-block;width:11px;height:11px;background:#fff;margin-right:8px;vertical-align:-1px;position:relative}
.btn{position:absolute;top:339px;height:38px;background:var(--green);color:#fff;font-weight:700;font-size:15px;text-align:center;line-height:38px;border-radius:2px}

/* I want band */
.band{left:0;top:872px;width:1200px;height:680px;background:var(--teal)}
.want{left:546px;top:901px;width:108px;height:108px;border-radius:50%;background:var(--teal-deep);color:#fff;font-weight:600;font-size:28px;line-height:30px;text-align:center;padding-top:22px}
.close{left:635px;top:906px;width:18px;height:18px;border-radius:50%;background:#222;color:#fff;font-size:11px;text-align:center;line-height:17px}
.tagline{left:0;top:1020px;width:1200px;text-align:center;color:#fff;font-size:20px}
.card{top:1086px;width:320px;height:394px;overflow:hidden}
.card .art{position:absolute;inset:0}
.card .cap{position:absolute;left:0;bottom:0;width:100%;height:52px;background:rgba(0,0,0,.55);color:#fff;font-size:20px;line-height:52px;padding-left:13px}
.card.dim .cap{color:#9a9a9a}
.arrow{top:1248px}

/* services */
.section-title{font-size:24px;color:var(--teal-text);font-weight:600;padding-left:13px;border-left:3px solid var(--teal-text);line-height:30px}
.services-title{left:109px;top:1563px}
.services-lead{left:126px;top:1596px;font-size:13px;color:#666}
.tab{top:1641px;height:50px;background:linear-gradient(#f4f4f4,#e2e2e2);border:1px solid #d4d4d4;font-size:16px;line-height:48px;color:#333}
.tab svg{position:absolute;left:12px;top:12px}
.tab span{position:absolute;left:78px}
.tab.active{background:var(--green);color:#fff;border-color:var(--green)}
.tab.active::after{content:"";position:absolute;left:0;bottom:-14px;border-style:solid;border-width:0 14px 14px 0;border-color:transparent #1f6e28 transparent transparent}
.tab-body{left:109px;top:1690px;width:980px;height:193px;border:1px solid var(--line)}
.tab-text{left:134px;top:1709px;width:630px;font-size:13px;line-height:22px;color:var(--muted)}
.more{left:134px;top:1848px;font-size:14px;font-weight:600;color:var(--teal-text)}
.video{left:799px;top:1705px;width:274px;height:163px;background:linear-gradient(135deg,#3d3a34,#1b1a18 60%,#4a4238)}
.play{left:913px;top:1764px;width:44px;height:44px;border-radius:50%;background:#fff}

/* welcome + testimonials */
.welcome-title{left:109px;top:1910px}
.welcome-text{left:126px;top:1946px;width:668px;font-size:13px;line-height:22px;color:var(--muted)}
.welcome-text p{margin-bottom:20px}
.testi-title{left:818px;top:1910px}
.person{left:836px;width:46px;height:46px;background:linear-gradient(#bdbdbd,#6f6f6f)}
.quote{left:893px;width:200px;font-size:12px;line-height:20px;color:var(--muted)}
.quote b{display:block;color:var(--green);font-weight:600;font-size:13px;margin-bottom:4px}

/* footer */
.footer{left:0;top:2188px;width:1200px;height:208px;background:var(--foot)}
.footer-base{left:0;top:2396px;width:1200px;height:50px;background:var(--foot-deep);color:#d0d0d0;font-size:12px}
.fcol{top:2208px;color:#fff;font-size:13px;line-height:23px}
.fcol h3{font-size:15px;font-weight:400;margin-bottom:12px;line-height:22px}
.fsep{top:2250px;width:1px;height:130px;background:#3a3f49}
</style>
</head>
<body>

<header>
  <div class="abs topbar"></div>
  <div class="abs brand">Lumavista</div>
  <div class="abs nav-assistant">My Assistant</div>
  <div class="abs nav-fav">My Favourites</div>
  <div class="abs search">Search..
    <svg width="17" height="17" viewBox="0 0 17 17"><circle cx="7" cy="7" r="5.5" fill="none" stroke="#fff" stroke-width="2.4"/><line x1="11" y1="11" x2="16" y2="16" stroke="#fff" stroke-width="2.6"/></svg>
  </div>
  <div class="abs avatar" role="img" aria-label="User profile portrait"></div>
  <div class="abs login">User Login <span style="font-size:9px;color:#aaa">▼</span></div>
  <div class="abs lang"><span class="flag"></span>English<span class="caret">▼</span></div>
</header>

<section>
  <div class="abs hero-photo" role="img" aria-label="Photo of a young couple with a city guidebook pointing at sights on a sunny European square"></div>
  <div class="abs fast-contact">FAST CONTACT</div>
  <div class="abs dot on">1</div>
  <div class="abs dot" style="top:460px"></div>
  <div class="abs dot" style="top:482px"></div>

  <form class="abs finder">
    <h1>FIND A PLACE TO STAY</h1>
    <p class="pitch">Exhibitions, museums, monuments<br>Tell us what you like,<br>We will tell you where to go!</p>
    <div class="field" style="left:9px;top:122px;width:299px">Where do you want to go?</div>
    <div class="field" style="left:9px;top:165px;width:299px">Persons</div>
    <div class="field" style="left:9px;top:207px;width:144px">Date</div>
    <div class="field" style="left:164px;top:207px;width:144px">Time</div>
    <div class="field" style="left:9px;top:249px;width:170px">Location</div>
    <div class="field" style="left:190px;top:249px;width:118px">Weather 16˚C</div>
    <div class="check" style="top:293px"><i></i>Обратно</div>
    <div class="check" style="top:312px"><i><svg width="11" height="11" viewBox="0 0 11 11" style="position:absolute;left:0;top:0"><path d="M2 5.5l2.5 2.5 4.5-5" fill="none" stroke="#222" stroke-width="1.6"/></svg></i>В одну сторону</div>
    <div class="btn" style="left:9px;width:142px">Click Here To Go</div>
    <div class="btn" style="left:164px;width:144px">What you want?</div>
  </form>
</section>

<section>
  <div class="abs band" role="img" aria-label="Teal band with a faint dotted world map"></div>
  <div class="abs want">I<br>Want</div>
  <div class="abs close">×</div>
  <div class="abs tagline">A Unique Approach To Search For Perfect Views</div>

  <svg class="abs arrow" style="left:46px" width="34" height="66" viewBox="0 0 34 66"><path d="M30 2L4 33l26 31" fill="none" stroke="#8fd0d5" stroke-width="4"/></svg>
  <svg class="abs arrow" style="left:1120px" width="34" height="66" viewBox="0 0 34 66"><path d="M4 2l26 31L4 64" fill="none" stroke="#8fd0d5" stroke-width="4"/></svg>

  <div class="abs card" style="left:109px">
    <div class="art" role="img" aria-label="Poster of a child reaching toward a kite over a city skyline with the hand-lettered words Reach Your Dreams" style="background:linear-gradient(#3f7f86 0%,#c9c79a 55%,#5f8b3a 80%,#2f5d24 100%)"></div>
    <div class="cap">Lumavista Dreams</div>
  </div>
  <div class="abs card dim" style="left:442px">
    <div class="art" role="img" aria-label="Photo of a tree trunk wrapped in colourful knitted yarn art" style="background:linear-gradient(160deg,#4e4a40,#6b3f52 45%,#3a5a4a 70%,#2f2e2a)"></div>
    <div class="cap">Lumavista Art</div>
  </div>
  <div class="abs card dim" style="left:771px">
    <div class="art" role="img" aria-label="Photo of a family playing together on a beach at dusk" style="background:linear-gradient(#3a3a3c,#5a4f4a 55%,#4a423e)"></div>
    <div class="cap">Lumavista Have Fun</div>
  </div>
</section>

<section>
  <h2 class="abs section-title services-title">Our Services</h2>
  <p class="abs services-lead">Lorem ipsum est simplement du faux texte employé dans la sition et la misen page avant impression employé sition et la misen page avant impression.</p>

  <div class="abs tab active" style="left:109px;width:244px">
    <svg width="40" height="26" viewBox="0 0 40 26"><rect x="1" y="1" width="38" height="24" fill="none" stroke="#fff" stroke-width="2"/><path d="M4 22l10-10 7 7 5-5 10 8z" fill="#fff"/><circle cx="29" cy="8" r="3" fill="#fff"/></svg>
    <span style="left:76px">Exhibitions</span>
  </div>
  <div class="abs tab" style="left:352px;width:239px">
    <svg width="36" height="30" viewBox="0 0 36 30"><path d="M18 1L2 9h32z" fill="#444"/><rect x="3" y="10" width="30" height="3" fill="#444"/><rect x="6" y="14" width="4" height="11" fill="#444"/><rect x="13" y="14" width="4" height="11" fill="#444"/><rect x="20" y="14" width="4" height="11" fill="#444"/><rect x="27" y="14" width="4" height="11" fill="#444"/><rect x="2" y="26" width="32" height="3" fill="#444"/></svg>
    <span style="left:80px">Museums</span>
  </div>
  <div class="abs tab" style="left:590px;width:240px">
    <svg width="34" height="24" viewBox="0 0 34 24" style="top:14px"><rect x="1" y="2" width="3" height="20" fill="#444"/><rect x="1" y="13" width="32" height="5" fill="#444"/><rect x="30" y="9" width="3" height="13" fill="#444"/><rect x="13" y="7" width="16" height="6" fill="#444"/><circle cx="8" cy="9" r="3" fill="#444"/></svg>
    <span style="left:63px">Hotel Service</span>
  </div>
  <div class="abs tab" style="left:829px;width:260px">
    <svg width="30" height="30" viewBox="0 0 30 30" style="top:10px"><path d="M4 26L18 12" stroke="#444" stroke-width="4"/><circle cx="21" cy="9" r="6" fill="none" stroke="#444" stroke-width="3"/><path d="M4 4l22 22" stroke="#444" stroke-width="3"/></svg>
    <span style="left:62px">Other Services</span>
  </div>

  <div class="abs tab-body"></div>
  <p class="abs tab-text">Lorem Ipsum est simplement du faux texte employé dans la sition et la misen page avant impression. Le Lorem Ipsum est le faux texte standard de l'imprimerie depuis les années 1500, quand un peintre anonyme assembla ensemble des morceaux de texte pour réaliser un livre spécimen de polices de texte. Il n'a pas fait que survivre cinq siècles, mais s'est aussi adapté à la bureautique informatique, sans que son contenu n'en soit modifié.<br>Il n'a pas fait que survivre cinq siècles, mais s'est aussi adapté à la bureautique informatique.</p>
  <div class="abs more">View Detail</div>
  <div class="abs video" role="img" aria-label="Video still of a visitor viewing framed artworks in a gallery"></div>
  <svg class="abs play" viewBox="0 0 44 44"><circle cx="22" cy="22" r="22" fill="#fff"/><path d="M17 13l13 9-13 9z" fill="#c0262d"/></svg>
</section>

<section>
  <h2 class="abs section-title welcome-title">Welcome to Lumavista</h2>
  <div class="abs welcome-text">
    <p>Lorem Ipsum est simplement du faux texte employé dans la sition et la misen page avant impression. Le Lorem Ipsum est le faux texte standard de l'imprimerie depuis les années 1500, quand un peintre anonyme assembla ensemble des morceaux de texte pour réaliser un livre spécimen de polices de texte.</p>
    <p>Il n'a pas fait que survivre cinq siècles, mais s'est aussi adapté à la bureautique informatique, sans que son contenu n'en soit modifié. Il a été popularisé dans les années 1960.</p>
    <p>grâce à la vente de feuilles Lettrafix contenant des passages du Lorem Ipsum, et, plus récemment, par son inclusion dans des applications de mise en page de texte, comme Folio Layout.</p>
  </div>

  <h2 class="abs section-title testi-title">Testimonials</h2>
  <div class="abs person" style="top:1951px" role="img" aria-label="Portrait of testimonial author"></div>
  <p class="abs quote" style="top:1950px"><b>Corwin Hale</b>"Lorem ipsum dolor sit nsectetuer adipiscing elit, sed diam nummy nibh euismod."</p>
  <div class="abs person" style="top:2047px" role="img" aria-label="Portrait of testimonial author"></div>
  <p class="abs quote" style="top:2046px"><b>Tobias Renwick</b>"Lorem ipsum dolor sit nsectetuer adipiscing elit, sed diam nummy nibh euismod. Nam magna pellentes de polices euismod."</p>
</section>

<footer>
  <div class="abs footer"></div>
  <div class="abs fsep" style="left:285px"></div>
  <div class="abs fsep" style="left:540px"></div>
  <div class="abs fsep" style="left:800px"></div>
  <div class="abs fcol" style="left:114px"><h3>DESTINATIONS:</h3>Europe<br>North America<br>South America<br>Africa<br>Asia<br>Australia</div>
  <div class="abs fcol" style="left:349px"><h3>SITE MAP</h3>Home<br>My Assistant<br>My Favourites<br>Language<br>Login</div>
  <div class="abs fcol" style="left:577px"><h3>OUR SERVICES</h3>Lorem ipsum dolor<br>Sit amet consecteture<br>Adipisicing elit<br>Son inclusin dans des</div>
  <div class="abs fcol" style="left:866px"><h3>CONTACT INFORMATIONS:</h3>E-mail: info@lumavista.example<br>Phone: +12 34 56 78 90<br>Opening hours:<br>Mon - Fri: 09.00 - 21.00<br>Sat: 12.00 - 16.00<br>Sun: 12.00 - 14.00</div>
  <div class="abs footer-base">
    <span class="abs" style="left:113px;top:16px">Copyright 2014 Lumavista. All Rights Reserved.</span>
    <span class="abs" style="left:866px;top:16px">Privacy Policy | Terms &amp; Condition</span>
  </div>
</footer>

</body>
</html>
```